Valbrook Data Works

Our company is about IT hardwares and IT solutions. IT hardware such as PC, RAMS, storage and servers. IT solutions such as project management, BA. We are also selling new technology too.

Target Market(s)

Consumer, Small to Medium Business, Corporate

Requirements
Must have
• The business card must have the following:
• Name:
• Title:
• Contact Number:
• Email address:
• Website:
• Color: Must match the logo color upgrade

```html
<!DOCTYPE html>
<html lang="en">
<head>
<meta charset="utf-8">
<title>Valbrook Data Works – Business Card</title>
<link href="https://fonts.googleapis.com/css2?family=Lato:wght@400;700;900&display=swap" rel="stylesheet">
<style>
  :root {
    --stage: #2b2b2b;
    --card-dark: #1f1f1f;
    --card-light: #ffffff;
    --accent: #e09a3a;
    --ink-light: #f2f2f2;
    --ink-dark: #3a3a3a;
  }
  * { box-sizing: border-box; margin: 0; padding: 0; }
  html, body {
    width: 1200px; height: 900px; overflow: hidden;
    background: var(--stage);
    font-family: "Lato", sans-serif;
  }
  .stage {
    position: relative; width: 1200px; height: 900px;
  }
  .card {
    position: absolute; left: 285px; width: 630px; height: 360px;
    overflow: hidden; background: var(--card-dark);
    box-shadow: 0 10px 30px rgba(0,0,0,.45);
  }
  .card--front { top: 60px; }
  .card--back { top: 480px; }

  /* Front */
  .brand {
    display: flex; align-items: center; gap: 14px;
    font-weight: 900; text-transform: uppercase; letter-spacing: 1px;
  }
  .brand__square { width: 22px; height: 22px; background: var(--accent); flex: none; }
  .front__brand {
    position: absolute; top: 140px; left: 0; right: 0;
    justify-content: center; color: var(--ink-light); font-size: 34px;
  }
  .front__web {
    position: absolute; top: 262px; left: 0; right: 0; text-align: center;
    color: var(--ink-light); font-size: 15px; letter-spacing: .5px;
  }

  /* Back */
  .back__shapes { position: absolute; inset: 0; }
  .person { position: absolute; left: 52px; top: 62px; }
  .person__name { color: var(--accent); font-size: 25px; font-weight: 700; }
  .person__title { color: var(--ink-light); font-size: 15px; margin-top: 2px; }
  .contacts { position: absolute; left: 52px; top: 140px; list-style: none; }
  .contacts li {
    display: flex; align-items: center; gap: 14px;
    color: var(--ink-light); font-size: 15px; line-height: 24px;
  }
  .contacts svg { width: 14px; height: 14px; fill: var(--accent); flex: none; }
  .address {
    position: absolute; left: 80px; top: 250px;
    color: var(--ink-light); font-size: 15px; line-height: 21px;
  }
  .back__brand {
    position: absolute; left: 445px; right: 18px; top: 140px;
    flex-direction: column; gap: 10px; text-align: center;
    color: var(--ink-dark); font-size: 24px; line-height: 1.1;
  }
</style>
</head>
<body>
<main class="stage">

  <section class="card card--front">
    <div class="brand front__brand">
      <span class="brand__square"></span>
      <span>Valbrook Data Works</span>
    </div>
    <p class="front__web">www.valbrookdata.com</p>
  </section>

  <section class="card card--back">
    <svg class="back__shapes" viewBox="0 0 630 360" aria-hidden="true">
      <path fill="var(--accent)" d="M424,0 C456,120 426,262 234,360 L630,360 L630,0 Z"/>
      <path fill="var(--card-light)" d="M440,0 C470,120 440,262 252,360 L630,360 L630,0 Z"/>
      <path fill="var(--accent)" d="M426,205 C410,290 320,340 150,360 L236,360 C360,318 412,282 426,205 Z"/>
    </svg>

    <div class="person">
      <h1 class="person__name">Daniel Ashcroft</h1>
      <p class="person__title">Manager</p>
    </div>

    <ul class="contacts">
      <li>
        <svg viewBox="0 0 24 24"><path d="M6.6 10.8a15 15 0 0 0 6.6 6.6l2.2-2.2c.3-.3.7-.4 1-.2 1.1.4 2.3.6 3.6.6.6 0 1 .4 1 1V20c0 .6-.4 1-1 1A17 17 0 0 1 3 4c0-.6.4-1 1-1h3.5c.6 0 1 .4 1 1 0 1.3.2 2.5.6 3.6.1.3 0 .7-.2 1z"/></svg>
        <span>555 014 2200</span>
      </li>
      <li>
        <svg viewBox="0 0 24 24"><path d="M6 2h12v5H6zM4 8h16a2 2 0 0 1 2 2v7h-4v5H6v-5H2v-7a2 2 0 0 1 2-2zm4 8v4h8v-4z"/></svg>
        <span>555 014 2201</span>
      </li>
      <li>
        <svg viewBox="0 0 24 24"><path d="M2 5h20v14H2zm2 2v.5l8 5 8-5V7l-8 5z"/></svg>
        <span>info@valbrookdata.com</span>
      </li>
      <li>
        <svg viewBox="0 0 24 24"><circle cx="12" cy="12" r="10"/></svg>
        <span>www.valbrookdata.com</span>
      </li>
    </ul>

    <p class="address">418 Carden Street<br>Millbrook, TX 75990</p>

    <div class="brand back__brand">
      <span class="brand__square"></span>
      <span>Valbrook Data Works</span>
    </div>
  </section>

</main>
</body>
</html>
```